Ridgemoor Partners

Need a new website - see more on ridgemoorpartners.com

Target Market(s)

Finance industry = conservative design

Coding

Coded - Design and coding required

Number of Pages Required

5+ page

Requirements
Should not have
• Dear all,
• Please avoid pictures of people on the website (except the "team" of course :-)

```html
<!DOCTYPE html>
<html lang="en">
<head>
<meta charset="utf-8">
<title>Ridgemoor Partners</title>
<link rel="stylesheet" href="https://fonts.googleapis.com/css2?family=Arimo:wght@400;700&display=swap">
<style>
  :root {
    --brand-red: #d8262c;
    --ink: #222222;
    --muted: #777777;
    --white: #ffffff;
    --bar-bg: #f1f1f1;
    --bar-line: #dcdcdc;
    --sky-top: #5d6579;
    --sky-blue: #7e8aa0;
    --cloud-warm: #b5ab98;
    --haze: #8f8e8a;
    --city-light: #7a6e62;
    --city-mid: #5b5048;
    --city-dark: #3b3531;
    --overlay: rgba(34, 38, 56, 0.38);
    --social: #8a8f99;
  }
  * { box-sizing: border-box; margin: 0; padding: 0; }
  html, body { width: 1200px; height: 676px; overflow: hidden; background: var(--white); }
  body { font-family: "Arimo", Helvetica, Arial, sans-serif; color: var(--ink); position: relative; }

  .hero {
    position: absolute; left: 0; top: 0; width: 1200px; height: 484px;
    background:
      radial-gradient(ellipse 260px 70px at 220px 150px, rgba(196,186,166,0.75), transparent 70%),
      radial-gradient(ellipse 320px 80px at 720px 130px, rgba(190,180,160,0.6), transparent 70%),
      radial-gradient(ellipse 240px 60px at 1060px 200px, rgba(185,176,158,0.6), transparent 70%),
      radial-gradient(ellipse 300px 70px at 480px 250px, rgba(176,168,150,0.5), transparent 70%),
      linear-gradient(180deg,
        var(--sky-top) 0%,
        var(--sky-blue) 22%,
        var(--cloud-warm) 45%,
        var(--haze) 55%,
        var(--city-light) 66%,
        var(--city-mid) 80%,
        var(--city-dark) 100%);
  }
  .hero::after {
    content: ""; position: absolute; inset: 0; background: var(--overlay);
  }

  .site-header {
    position: absolute; left: 0; top: 0; width: 1200px; height: 74px;
    border-bottom: 1px solid rgba(255,255,255,0.4);
    display: flex; align-items: center; padding: 0 32px 0 58px; z-index: 2;
  }
  .brand { display: flex; align-items: center; gap: 10px; color: var(--white); text-decoration: none; width: 300px; }
  .brand-mark { width: 44px; height: 44px; border-radius: 50%; background: var(--brand-red); }
  .brand-name { font-size: 13px; font-weight: 400; line-height: 13px; letter-spacing: 0.01em; text-transform: uppercase; }
  .main-nav { display: flex; gap: 36px; margin-left: 70px; }
  .main-nav a { color: var(--white); text-decoration: none; font-weight: 700; font-size: 14px; text-transform: uppercase; }
  .header-actions { margin-left: auto; display: flex; gap: 6px; }
  .btn-pill { font-size: 13px; padding: 7px 11px; border-radius: 16px; text-decoration: none; }
  .btn-outline { color: var(--white); border: 1px solid var(--white); }
  .btn-solid { background: var(--white); color: var(--ink); border: 1px solid var(--white); }

  .sub-bar {
    position: absolute; left: 0; top: 484px; width: 1200px; height: 32px;
    background: var(--bar-bg); border-bottom: 1px solid var(--bar-line);
    display: flex; align-items: center; padding: 0 50px 0 52px; font-size: 12px; color: var(--muted);
  }
  .sub-bar .label { margin-right: 12px; }
  .sub-bar a { color: var(--muted); text-decoration: none; margin-right: 24px; }
  .sub-tools { margin-left: auto; display: flex; align-items: center; gap: 22px; }
  .social-dot { width: 14px; height: 14px; border-radius: 2px; background: var(--social); }

  .intro { position: absolute; left: 0; top: 534px; width: 1200px; text-align: center; }
  .intro h1 { font-size: 20px; font-weight: 400; line-height: 27px; }
  .intro p { font-size: 12px; color: #444; margin-top: 10px; }
  .btn-learn {
    display: inline-flex; align-items: center; gap: 8px; margin-top: 15px;
    color: var(--brand-red); border: 1px solid var(--brand-red); border-radius: 18px;
    padding: 10px 18px; font-size: 13px; font-weight: 700; text-decoration: none;
  }
</style>
</head>
<body>
  <div class="hero" role="img" aria-label="Photograph of a financial district skyline under a cloudy sky"></div>

  <header class="site-header">
    <a class="brand" href="#"><span class="brand-mark"></span><span class="brand-name">Ridgemoor<br>Partners</span></a>
    <nav class="main-nav">
      <a href="#">Our Services</a>
      <a href="#">News</a>
      <a href="#">Team</a>
      <a href="#">Contact</a>
    </nav>
    <div class="header-actions">
      <a class="btn-pill btn-outline" href="#">Log In</a>
      <a class="btn-pill btn-solid" href="#">Current Engagements</a>
    </div>
  </header>

  <div class="sub-bar">
    <span class="label">Learn More:</span>
    <a href="#">Our Company</a>
    <a href="#">Careers</a>
    <a href="#">Help &amp; Contact</a>
    <div class="sub-tools">
      <span class="social-dot"></span>
      <span class="social-dot"></span>
      <span class="social-dot"></span>
      <svg width="13" height="13" viewBox="0 0 13 13" aria-label="Search"><circle cx="5.5" cy="5.5" r="4" fill="none" stroke="#8a8f99" stroke-width="1.6"/><line x1="8.5" y1="8.5" x2="12" y2="12" stroke="#8a8f99" stroke-width="1.8"/></svg>
    </div>
  </div>

  <section class="intro">
    <h1>Founded in 2004, Ridgemoor is headquartered in Gibraltar<br>with representative offices in Luxembourg and London</h1>
    <p>See some of the features below and learn why businesses trust Ridgemoor</p>
    <a class="btn-learn" href="#">
      <svg width="9" height="10" viewBox="0 0 9 10"><polygon points="0,0 9,5 0,10" fill="#d8262c"/></svg>
      Learn about Ridgemoor
    </a>
  </section>
</body>
</html>
```